Lumen Beauty & Spa Business Card Design

Hello, I have a Beauty salon On my own Property. It is a Balinese Style Salon with a Spa & Sauna together with all beauty Options available. I have strived myself to get trained In Indonesia as well as here so I can offer my clients something "unique & special" somewhere to unwind as well as be pampered and step out of reality for even a little while.

So with all this in mind I would like to keep everything on the "natural style look" if possible....

I was hoping to have some kind Of Kraft look paper or background look, with a Olive/lime Natural Green colour Logo and Name on the front. "Lumen Beauty & Spa"

Details (im really not sure on how it should be placed on the card whether back or front?)
I'd really like written somewhere on the card, somewhere
.... Lumen Daydream ...

also if room maybe a few things that I do eg. Waxing, Tanning, teeth Whitening, all kinds of Beauty and much more.

DETAILS are
Lumen Beauty & Spa
Marisa Pellow
Ph: 04 873 21 560
Address: 12 Tarrow Court
Fernwick NSW 2391

(facebook logo) www.facenook.example/LumenBeautySpa

I think this is all the info that I need on the card.. if I have forgotten anything or if you need anything else please dont hesitate to contact me....
& just maybe a few dotted lines so I can write appt times etc.. I was also thinking maybe a QR BarCode. Sorry this is the first time I have done any business cards so forgive me I dont really have a clue.

please let me know what else you need me to do from here thanks for your time.
Risa

Industry/Entity Type

Salon

Font styles to use
Script

Colors
acd036
9bcb3c

```html
<!DOCTYPE html>
<html lang="en">
<head>
<meta charset="utf-8">
<title>Lumen Beauty &amp; Spa – Business Card</title>
<link href="https://fonts.googleapis.com/css2?family=Great+Vibes&family=Open+Sans:wght@400;600&display=swap" rel="stylesheet">
<style>
  :root{
    --lime:#acd036;
    --leaf:#9bcb3c;
    --mint:#5cc98a;
    --deep:#3fb34f;
    --rose:#e0395a;
    --ink:#1e1e1e;
    --card:#ffffff;
    --stage:#efeae2;
  }
  *{margin:0;padding:0;box-sizing:border-box}
  html,body{width:1200px;height:1023px;overflow:hidden;background:var(--stage)}
  .stage{position:relative;width:1200px;height:1023px}
  .card{
    position:absolute;left:250px;width:700px;height:400px;
    background:var(--card);border-radius:18px;overflow:hidden;
    box-shadow:0 6px 24px rgba(0,0,0,.12);
  }
  .card--front{top:80px}
  .card--back{top:543px}
  .card__art{position:absolute;inset:0;width:100%;height:100%}
  .script{font-family:"Great Vibes",cursive;font-weight:400}
  .sans{font-family:"Open Sans",sans-serif}

  /* front */
  .brand{position:absolute;color:var(--mint);line-height:1;white-space:nowrap}
  .brand__name{font-size:100px}
  .brand__tag{font-size:42px;margin-left:10px}
  .card--front .brand{left:200px;top:90px}
  .owner{position:absolute;left:330px;top:196px;font-size:40px;color:var(--rose)}
  .contact{position:absolute;left:330px;top:246px;color:var(--ink);font-size:16px;line-height:26px}
  .contact__phone{padding-left:110px}

  /* back */
  .appt{position:absolute;left:40px;top:30px;width:420px}
  .appt__title{font-size:26px;font-weight:600;color:var(--leaf)}
  .appt__field{display:flex;align-items:flex-end;font-size:22px;color:var(--ink);margin-top:6px}
  .appt__line{flex:1;margin-left:8px;margin-bottom:6px;border-bottom:2px dotted #9a9a9a}
  .services{position:absolute;left:40px;top:150px;font-size:17px;line-height:24px;color:var(--leaf)}
  .card--back .brand{left:40px;top:250px;color:var(--leaf)}
  .card--back .brand__name{font-size:80px}
  .card--back .brand__tag{font-size:34px}
</style>
</head>
<body>
<main class="stage">

  <section class="card card--front" aria-label="Card front">
    <svg class="card__art" viewBox="0 0 700 400" aria-hidden="true">
      <defs>
        <linearGradient id="bandLime" x1="0" y1="0" x2="1" y2="1">
          <stop offset="0" stop-color="#9bcb3c"/>
          <stop offset="1" stop-color="#c8e27a"/>
        </linearGradient>
      </defs>
      <path d="M0,0 H190 C120,70 120,170 220,250 C140,225 60,240 0,300 Z" fill="url(#bandLime)"/>
      <path d="M0,0 H150 C95,60 95,150 170,225 C110,210 50,220 0,250 Z" fill="#ffffff" opacity=".35"/>
      <path d="M700,150 C610,250 470,330 380,400 H700 Z" fill="url(#bandLime)"/>
      <path d="M700,190 C620,270 500,340 440,400 H460 C530,345 640,270 700,215 Z" fill="#ffffff" opacity=".5"/>
      <path d="M520,0 C580,20 640,10 700,0 Z" fill="#c8e27a"/>
      <circle cx="630" cy="40" r="16" fill="none" stroke="#acd036" stroke-width="6"/>
    </svg>
    <svg class="card__art" viewBox="0 0 700 400">
      <path role="img" aria-label="Illustration of a profile silhouette formed from green leaves and flourishes"
            d="M40,230 C120,200 230,220 330,300 C300,350 260,385 220,400 H40 Z"
            fill="url(#illusFront)"/>
      <defs>
        <linearGradient id="illusFront" x1="0" y1="0" x2="1" y2="1">
          <stop offset="0" stop-color="#3fb34f"/>
          <stop offset="1" stop-color="#8fd6a6"/>
        </linearGradient>
      </defs>
    </svg>

    <div class="brand script"><span class="brand__name">Lumen</span><span class="brand__tag">Beauty &amp; Spa</span></div>
    <p class="owner script">Marisa Pellow</p>
    <address class="contact sans" style="font-style:normal">
      <span class="contact__phone">04 873 21 560</span><br>
      12 Tarrow Court, Fernwick NSW 2391
    </address>
  </section>

  <section class="card card--back" aria-label="Card back">
    <svg class="card__art" viewBox="0 0 700 400">
      <defs>
        <linearGradient id="illusBack" x1="0" y1="1" x2="1" y2="0">
          <stop offset="0" stop-color="#9bcb3c"/>
          <stop offset="1" stop-color="#c8e27a"/>
        </linearGradient>
      </defs>
      <path role="img" aria-label="Illustration of green leaves and a profile silhouette among flourishes"
            d="M330,400 C380,320 470,270 560,250 C620,240 670,250 700,230 V400 Z"
            fill="url(#illusBack)"/>
      <circle cx="660" cy="270" r="14" fill="none" stroke="#acd036" stroke-width="5" aria-hidden="true"/>
    </svg>

    <div class="appt sans">
      <p class="appt__title">Appointment:</p>
      <p class="appt__field">Date:<span class="appt__line"></span></p>
      <p class="appt__field">Time:<span class="appt__line"></span></p>
    </div>
    <p class="services sans">Waxing | Tanning | Teeth Whitening<br>all kinds of Beauty and much more.</p>
    <div class="brand script"><span class="brand__name">Lumen</span><span class="brand__tag">Beauty &amp; Spa</span></div>
  </section>

</main>
</body>
</html>
```